Stationary pack for Corvalen

Corvalen is a recently establish Solar brokerage company based in Australia. We have a number of sales staff who provide advice and guidance to both residential and commercial customers regarding solar systems (solar hot water and solar panels.)

In addition to our brokerage services we are also developing software for the solar industry, which will be used to automate the solar system install process. This system will be used by other companies in the solar industry including installers, wholesalers and government departments.

We are after a stationary pack that consists of the following: Business cards, compliments slip and letter head.

The EPS, AI, PNG etc files for the logo are attached.

For the business card:
The name and logo of the company need to be clearly visible. On the back of the business cards, we would like the logo. I am happy for you to split the image part of the logo from the text if you think it would look better a different way.

I would like the business cards to be easily readable with the following information on the front:
Name
(Please leave room for titles for the future – eg Sales Advisor.)
Mobile
Office
Email
Address
ABN

Letter heads:
I would prefer the address to be at the top

Compliments slips:
Only need to be one sided

Target Market(s)

Corvalen provides services to both residential and commercial customers. Our customers will be environmentally conscious.

Industry/Entity Type

Residential

Requirements
Must have
• Business cards must have the logo on the back.

```html
<!DOCTYPE html>
<html lang="en">
<head>
<meta charset="utf-8">
<title>Corvalen Stationery Pack</title>
<link rel="stylesheet" href="https://fonts.googleapis.com/css2?family=Arimo:wght@700&family=Inconsolata:wght@400&display=swap">
<style>
  :root {
    --brand-green: #4e9c3a;
    --brand-blue: #2f4f8c;
    --paper: #ffffff;
    --canvas: #ffffff;
    --ink-soft: #a8a8a8;
    --wash: #eef5ea;
    --shadow: rgba(0, 0, 0, 0.6);
  }
  * { box-sizing: border-box; margin: 0; padding: 0; }
  html, body { width: 1200px; height: 900px; overflow: hidden; background: var(--canvas); }
  .stage { position: relative; width: 1200px; height: 900px; }

  .sheet {
    position: absolute;
    background: var(--paper);
    box-shadow: 5px 5px 5px var(--shadow);
    overflow: hidden;
  }
  .wordmark {
    font-family: "Arimo", Arial, sans-serif;
    font-weight: 700;
    color: var(--brand-green);
    letter-spacing: -0.02em;
    line-height: 1;
    white-space: nowrap;
  }
  .brand-dot {
    display: block;
    border-radius: 50%;
    background: var(--brand-green);
  }
  .fine-print {
    font-family: "Inconsolata", "Courier New", monospace;
    color: var(--ink-soft);
    line-height: 1.25;
    white-space: nowrap;
  }

  /* Letterhead */
  .letterhead { left: 512px; top: 15px; width: 493px; height: 697px; }
  .letterhead .wash {
    position: absolute; inset: 0;
    background: radial-gradient(ellipse 80% 95% at 100% 70%, var(--wash) 0%, var(--wash) 50%, rgba(238,245,234,0) 80%);
  }
  .letterhead .header {
    position: absolute; left: 146px; top: 27px; width: 200px;
    display: flex; flex-direction: column; align-items: center;
  }
  .letterhead .brand-dot { width: 38px; height: 38px; }
  .letterhead .wordmark { font-size: 21px; margin-top: 4px; }
  .letterhead .fine-print { font-size: 7px; text-align: center; margin-top: 6px; }

  /* Business cards */
  .card { left: 287px; width: 210px; height: 125px; }
  .card-front { top: 352px; }
  .card-back { top: 489px; display: flex; flex-direction: column; align-items: center; justify-content: center; gap: 6px; }
  .card-front .wordmark { position: absolute; left: 9px; top: 13px; font-size: 32px; }
  .card-front .fine-print { position: absolute; left: 9px; top: 58px; font-size: 5.5px; }
  .card-front .fine-print p + p { margin-top: 5px; }
  .card-back .brand-dot { width: 64px; height: 64px; }
  .card-back .wordmark { font-size: 16px; }

  /* Compliments slip */
  .comp-slip { left: 213px; top: 627px; width: 510px; height: 248px; }
  .comp-slip .wash {
    position: absolute; inset: 0;
    background: radial-gradient(ellipse 65% 95% at 30% 110%, var(--wash) 0%, var(--wash) 45%, rgba(238,245,234,0) 78%);
  }
  .comp-slip .brand {
    position: absolute; left: 31px; top: 18px; width: 84px;
    display: flex; flex-direction: column; align-items: center;
  }
  .comp-slip .brand-dot { width: 38px; height: 38px; }
  .comp-slip .wordmark { font-size: 19px; margin-top: 3px; }
  .comp-slip .fine-print { position: absolute; left: 31px; top: 88px; font-size: 7px; }
  .comp-slip .fine-print p + p { margin-top: 9px; }
  .comp-slip .closing {
    position: absolute; left: 31px; top: 195px;
    font-family: "Arimo", Arial, sans-serif; font-weight: 700;
    font-size: 8px; color: var(--brand-blue); letter-spacing: -0.01em;
  }
</style>
</head>
<body>
<main class="stage">

  <section class="sheet letterhead" aria-label="Letterhead">
    <div class="wash" role="img" aria-label="Faint green brand decoration"></div>
    <header class="header">
      <span class="brand-dot"></span>
      <div class="wordmark">Corvalen</div>
      <p class="fine-print">45 Sunlit Road . Town . Postcode<br>01632 960 412</p>
    </header>
  </section>

  <section class="sheet card card-front" aria-label="Business card front">
    <div class="wordmark">Corvalen</div>
    <div class="fine-print">
      <p>Alex Carter - Sales Advisor<br>Email: a.carter@corvalen-mail.test<br>Mobile: 07700 900 318</p>
      <p>45 Sunlit Road<br>Town, postcode<br>T: 01632 960 412<br>ABN</p>
    </div>
  </section>

  <section class="sheet card card-back" aria-label="Business card back">
    <span class="brand-dot"></span>
    <div class="wordmark">Corvalen</div>
  </section>

  <section class="sheet comp-slip" aria-label="Compliments slip">
    <div class="wash" role="img" aria-label="Faint green brand decoration"></div>
    <div class="brand">
      <span class="brand-dot"></span>
      <div class="wordmark">Corvalen</div>
    </div>
    <div class="fine-print">
      <p>45 Sunlit Road<br>Town, postcode</p>
      <p>T: 01632 960 412</p>
      <p>info@corvalen-mail.test<br>www.corvalen-site.test</p>
    </div>
    <p class="closing">WITH COMPLIMENTS</p>
  </section>

</main>
</body>
</html>
```